Management consulting Company in the electronic payment ecosystem needs a Website

We need to have a "showcase" style website that contains the key message that our company is able to provide management consulting in the world of payment systems. Our mission is to assist our clients in reviewing their sales, purchasing, operation and IT processes and to support them in identifying the best solution in the use of payment systems.

```html
<!DOCTYPE html>
<html lang="en">
<head>
<meta charset="utf-8">
<title>Veltra Consulting — Payment Systems Management Consulting</title>
<link rel="stylesheet" href="https://fonts.googleapis.com/css2?family=Raleway:wght@400;500;600;700&display=swap">
<style>
  :root {
    --navy: #0b1547;
    --navy-deep: #08103a;
    --ink: #111a4a;
    --text: #2a2a35;
    --white: #ffffff;
    --mist: #f4f1f2;
    --footer: #1d1c20;
    --accent: #f2b24a;
  }
  * { margin: 0; padding: 0; box-sizing: border-box; }
  html, body { width: 1200px; height: 4115px; overflow: hidden; }
  body { font-family: "Raleway", sans-serif; color: var(--text); background: var(--white); position: relative; }
  .abs { position: absolute; }
  .btn { position: absolute; display: flex; align-items: center; justify-content: center; background: var(--navy); color: var(--white); font-weight: 700; border-radius: 4px; font-size: 11px; }
  .btn-flow { position: static; display: inline-flex; }

  /* Header / hero */
  .hero { top: 0; left: 0; width: 1200px; height: 671px; background: linear-gradient(135deg, #4a5590 0%, #2e3670 45%, #3c4478 70%, #1f2658 100%); }
  .hero-photo { position: absolute; inset: 0; background: radial-gradient(ellipse at 55% 35%, rgba(190,195,225,.35), transparent 60%), radial-gradient(ellipse at 80% 60%, rgba(20,25,60,.5), transparent 60%); }
  .brand { display: flex; align-items: center; gap: 10px; color: var(--white); font-weight: 700; font-size: 30px; white-space: nowrap; }
  .brand-mark { width: 36px; height: 36px; border-radius: 50%; border: 5px solid currentColor; }
  .main-nav { top: 30px; right: 130px; display: flex; gap: 42px; color: var(--white); font-size: 17px; font-weight: 600; white-space: nowrap; }
  .hero-title { top: 283px; width: 100%; text-align: center; color: var(--white); font-size: 46px; font-weight: 600; }
  .hero-sub { top: 355px; width: 100%; text-align: center; color: var(--white); font-size: 18px; }
  .hero-btn { top: 425px; left: 532px; width: 134px; height: 48px; border: 3px solid var(--white); border-radius: 8px; color: var(--white); font-size: 17px; font-weight: 600; display: flex; align-items: center; justify-content: center; }
  .dots { top: 627px; left: 562px; display: flex; gap: 10px; align-items: center; }
  .dots span { width: 7px; height: 7px; border-radius: 50%; background: var(--white); }
  .dots .on { width: 13px; height: 13px; background: var(--accent); border: 2px solid var(--white); }

  .stats { top: 671px; left: 0; width: 1200px; height: 142px; background: var(--navy-deep); color: var(--white); }
  .stat { position: absolute; top: 36px; text-align: center; }
  .stat b { display: block; font-weight: 400; font-size: 30px; }
  .stat small { display: block; font-size: 16px; margin-top: 6px; }

  /* Services */
  .section-title { color: var(--ink); font-weight: 700; font-size: 30px; white-space: nowrap; }
  .services-intro { top: 952px; left: 131px; width: 260px; }
  .services-intro .rule { width: 52px; height: 3px; background: var(--ink); margin: 12px 0 40px; }
  .services-intro p { color: var(--ink); font-size: 17px; font-weight: 600; line-height: 26px; }
  .service-card { position: absolute; width: 300px; height: 337px; background: var(--white); box-shadow: 0 0 14px rgba(0,0,0,.08); text-align: center; }
  .service-card svg { margin-top: 40px; }
  .service-card h3 { color: var(--ink); font-size: 19px; font-weight: 700; margin-top: 14px; }
  .service-card p { font-size: 12.5px; line-height: 18px; width: 214px; margin: 18px auto 0; color: #333; }
  .service-card .btn { left: 108px; bottom: 36px; width: 84px; height: 30px; }

  /* About */
  .about { top: 1618px; left: 0; width: 1200px; height: 472px; background: var(--mist); }
  .about-photo { position: absolute; right: 0; top: 0; width: 680px; height: 472px; background: linear-gradient(90deg, var(--mist) 0%, #d9dde4 25%, #b8c2d2 60%, #8894a8 100%); }
  .eyebrow { color: var(--ink); font-size: 21px; font-weight: 600; }
  .about-head { color: var(--ink); font-size: 29px; font-weight: 700; line-height: 38px; margin-top: 14px; }
  .body-copy { font-size: 15.5px; line-height: 24px; color: var(--text); }

  /* Benefits */
  .benefit { position: absolute; top: 2222px; width: 296px; height: 257px; background: var(--navy-deep); color: var(--white); text-align: center; }
  .benefit svg { margin-top: 28px; }
  .benefit h3 { font-size: 21px; font-weight: 600; margin-top: 20px; }
  .benefit p { font-size: 12.5px; line-height: 18px; width: 230px; margin: 18px auto 0; color: #d8daea; }

  /* Payments */
  .payments { top: 2538px; left: 0; width: 1200px; height: 456px; background: var(--mist); }
  .payments-photo { position: absolute; left: 0; top: 0; width: 591px; height: 456px; background: linear-gradient(135deg, #e8e2da 0%, #c7c2bd 40%, #7b8090 75%, #3a3c48 100%); }

  /* Blog */
  .post { position: absolute; top: 3129px; width: 297px; height: 386px; background: var(--navy-deep); color: var(--white); }
  .post-photo { height: 165px; }
  .post h3 { font-size: 16.5px; font-weight: 700; line-height: 23px; margin: 30px 27px 0; }
  .post p { font-size: 12.5px; line-height: 17px; margin: 14px 27px 0; color: #d8daea; }
  .post .btn { left: 27px; top: 326px; width: 78px; height: 28px; background: var(--white); color: var(--navy); }

  /* CTA */
  .cta { top: 3574px; left: 0; width: 1200px; height: 332px; background: var(--mist); text-align: center; }

  /* Footer */
  .footer { top: 3906px; left: 0; width: 1200px; height: 209px; background: var(--footer); color: var(--white); }
  .footer .brand { font-size: 56px; gap: 16px; }
  .footer .brand-mark { width: 88px; height: 88px; border-width: 9px; }
  .social { display: flex; gap: 10px; align-items: center; }
  .social span { width: 26px; height: 26px; border-radius: 50%; background: #2f6fd6; }
</style>
</head>
<body>

<header class="abs hero">
  <div class="hero-photo" role="img" aria-label="Photo of a consultant working on a laptop at a desk, blue-tinted"></div>
  <div class="abs brand" style="top:22px;left:133px;"><span class="brand-mark"></span>Veltra Consulting</div>
  <nav class="abs main-nav"><span>Home</span><span>About Us</span><span>Services</span><span>Blog</span><span>Contact Us</span></nav>
  <h1 class="abs hero-title">Management Consulting</h1>
  <p class="abs hero-sub">Lorem Ipsum is simply dummy text of the printing and typesetting industry</p>
  <div class="abs hero-btn">Read More</div>
  <div class="abs dots"><span></span><span></span><span class="on"></span><span></span><span></span></div>
</header>

<section class="abs stats">
  <div class="stat" style="left:134px;width:140px;"><b>10+</b><small>Years Experienced</small></div>
  <div class="stat" style="left:530px;width:140px;"><b>43%</b><small>Lorem Ipsum</small></div>
  <div class="stat" style="left:846px;width:236px;"><b>73.000+</b><small>Professionals in our network</small></div>
</section>

<section class="abs services-intro">
  <h2 class="section-title">Our Services</h2>
  <div class="rule"></div>
  <p>Lorem Ipsum is simply dummy text of the printing and type setting industry.</p>
</section>

<article class="service-card" style="top:866px;left:449px;">
  <svg width="70" height="62" viewBox="0 0 70 62" fill="none" stroke="#0b1547" stroke-width="4"><rect x="4" y="8" width="50" height="36"/><path d="M29 44v10M18 56h22"/><circle cx="48" cy="16" r="12" fill="#fff"/><path d="M56 25l10 10"/></svg>
  <h3>Analysis</h3>
  <p>Lorem Ipsum is simply dummy text of the printing and typesetting industry. Lorem Ipsum has been the industry's</p>
  <div class="btn">Read More</div>
</article>
<article class="service-card" style="top:866px;left:768px;">
  <svg width="62" height="62" viewBox="0 0 62 62" fill="none" stroke="#0b1547" stroke-width="4"><circle cx="31" cy="31" r="24" stroke-dasharray="8 4"/><circle cx="31" cy="31" r="10"/><path d="M31 31l10-14"/></svg>
  <h3>Optimization</h3>
  <p>Lorem Ipsum is simply dummy text of the printing and typesetting industry. Lorem Ipsum has been the industry's</p>
  <div class="btn">Read More</div>
</article>
<article class="service-card" style="top:1224px;left:133px;">
  <svg width="70" height="66" viewBox="0 0 70 66" fill="none" stroke="#0b1547" stroke-width="3"><rect x="4" y="4" width="48" height="56"/><path d="M12 16h10M12 28h10M12 40h10M28 16h16M28 28h12"/><circle cx="52" cy="40" r="12" fill="#fff"/><path d="M56 52v10"/></svg>
  <h3>Overview</h3>
  <p>Lorem Ipsum is simply dummy text of the printing and typesetting industry. Lorem Ipsum has been the industry's</p>
  <div class="btn">Read More</div>
</article>
<article class="service-card" style="top:1224px;left:449px;">
  <svg width="74" height="62" viewBox="0 0 74 62" fill="none" stroke="#0b1547" stroke-width="4"><rect x="4" y="4" width="66" height="42"/><path d="M37 46v8M24 58h26"/><circle cx="22" cy="25" r="8"/><path d="M40 34v-10M48 34v-16M56 34v-12"/></svg>
  <h3>Monitoring</h3>
  <p>Lorem Ipsum is simply dummy text of the printing and typesetting industry. Lorem Ipsum has been the industry's</p>
  <div class="btn">Read More</div>
</article>
<article class="service-card" style="top:1224px;left:768px;">
  <svg width="70" height="62" viewBox="0 0 70 62" fill="#0b1547"><path d="M22 4h44v30H52l-8 8v-8H22z"/><path d="M4 18h30v30H18l-8 10v-10H4z" stroke="#fff" stroke-width="3"/></svg>
  <h3>Payments Consultancy</h3>
  <p>Lorem Ipsum is simply dummy text of the printing and typesetting industry. Lorem Ipsum has been the industry's</p>
  <div class="btn">Read More</div>
</article>

<section class="abs about">
  <div class="about-photo" role="img" aria-label="Photo of a smiling professional working on a laptop in a bright office"></div>
  <div class="abs" style="top:48px;left:132px;width:430px;">
    <p class="eyebrow">About us</p>
    <h2 class="about-head">We empower &amp; connect<br>payment professionals<br>to facilitate growth.</h2>
    <p class="body-copy" style="margin-top:22px;">There are many variations of passages of Lorem Ipsum available, but the majority have suffered alteration in some form, by injected humour, or randomised words which don't look even slightly believable. If you are going to use a passage of Lorem Ipsum, you need to be sure there isn't anything embarrassing.</p>
    <div class="btn btn-flow" style="margin-top:28px;width:90px;height:31px;">Read More</div>
  </div>
</section>

<h2 class="abs section-title" style="top:2142px;width:100%;text-align:center;font-weight:600;">Straightforward Payment Consulting</h2>
<article class="benefit" style="left:133px;">
  <svg width="70" height="66" viewBox="0 0 70 66" fill="none" stroke="#fff" stroke-width="3"><circle cx="42" cy="36" r="22"/><path d="M42 36l8-10M38 8h8M4 28h18M8 38h14M12 48h14"/></svg>
  <h3>Save Time</h3>
  <p>Lorem Ipsum is simply dummy text of the printing and typesetting industry. Lorem Ipsum.</p>
</article>
<article class="benefit" style="left:453px;">
  <svg width="70" height="66" viewBox="0 0 70 66" fill="none" stroke="#fff" stroke-width="3"><path d="M12 62V20M6 26l6-8 6 8M35 62V8M29 14l6-8 6 8M58 62V20M52 26l6-8 6 8"/><circle cx="35" cy="46" r="10" fill="#08103a"/></svg>
  <h3>Grow your business</h3>
  <p>Lorem Ipsum is simply dummy text of the printing and typesetting industry. Lorem Ipsum.</p>
</article>
<article class="benefit" style="left:773px;">
  <svg width="70" height="66" viewBox="0 0 70 66" fill="none" stroke="#fff" stroke-width="3"><circle cx="35" cy="30" r="24" stroke-dasharray="7 4"/><circle cx="35" cy="26" r="9"/><path d="M20 50c4-10 26-10 30 0M24 26h-4v8h4M46 26h4v8h-4"/></svg>
  <h3>Friendly support</h3>
  <p>Lorem Ipsum is simply dummy text of the printing and typesetting industry. Lorem Ipsum.</p>
</article>

<section class="abs payments">
  <div class="payments-photo" role="img" aria-label="Photo of hands using a tablet beside a laptop showing charts"></div>
  <div class="abs" style="top:82px;left:660px;width:380px;">
    <h2 class="section-title" style="font-weight:600;">We are all about payments</h2>
    <p class="body-copy" style="margin-top:22px;">There are many variations of passages of Lorem Ipsum available, but the majority have suffered alteration in some form, by injected humour, or randomised words which don't look even slightly believable. If you are going to use a passage of Lorem Ipsum, you need to be sure there isn't anything embarrassing.</p>
    <div class="btn btn-flow" style="margin-top:28px;width:89px;height:32px;">Read More</div>
  </div>
</section>

<h2 class="abs section-title" style="top:3048px;width:100%;text-align:center;font-weight:600;">Latest Blog</h2>
<article class="post" style="left:133px;">
  <div class="post-photo" role="img" aria-label="Photo of a presenter at a whiteboard in a meeting" style="background:linear-gradient(135deg,#e9ecef,#a9b4c2 60%,#5d6a80);"></div>
  <h3>Lorem Ipsum is simply dum my text of the printing</h3>
  <p>There are many variations of passages of Lorem Ipsum available, but the majority have suffered .</p>
  <div class="btn">Read More</div>
</article>
<article class="post" style="left:453px;">
  <div class="post-photo" role="img" aria-label="Photo of hands writing in a notebook beside a laptop" style="background:linear-gradient(135deg,#f0efec,#bfc3c8 55%,#6b7080);"></div>
  <h3>Lorem Ipsum is simply dum my text of the printing</h3>
  <p>There are many variations of passages of Lorem Ipsum available, but the majority have suffered .</p>
  <div class="btn">Read More</div>
</article>
<article class="post" style="left:773px;">
  <div class="post-photo" role="img" aria-label="Photo of rising bar chart with a warm glow" style="background:linear-gradient(135deg,#1c1a22,#6a5a3a 55%,#e8b34a);"></div>
  <h3>Lorem Ipsum is simply dum my text of the printing</h3>
  <p>There are many variations of passages of Lorem Ipsum available, but the majority have suffered .</p>
  <div class="btn">Read More</div>
</article>

<section class="abs cta">
  <h2 class="section-title" style="font-size:26px;font-weight:600;line-height:35px;margin-top:56px;">Lorem Ipsum is simply dummy text of<br>the printing and typesetting industry</h2>
  <p class="body-copy" style="width:560px;margin:22px auto 0;font-size:16px;">There are many variations of passages of Lorem Ipsum available, but the majority have suffered alteration in some form, by injected humour, or randomised words which don't look even slightly believable.</p>
  <div class="btn" style="top:246px;left:551px;width:102px;height:35px;font-size:13px;">Contact Us</div>
</section>

<footer class="abs footer">
  <div class="abs brand" style="top:56px;left:133px;"><span class="brand-mark"></span>Veltra</div>
  <div class="abs" style="top:56px;right:120px;display:flex;gap:14px;align-items:center;font-size:12px;">
    FOLLOW US
    <div class="social" aria-label="Social links"><span></span><span></span><span></span></div>
  </div>
  <nav class="abs main-nav" style="top:106px;right:129px;gap:46px;font-weight:500;"><span>Home</span><span>About Us</span><span>Services</span><span>Blog</span><span>Contact Us</span></nav>
  <p class="abs" style="top:156px;right:130px;font-size:11px;">Copyright © 2021 All Rights Reserved</p>
</footer>

</body>
</html>
```